RV Solvents Needs a Product Brochure Design

RV Solvents is a specialty chemical company that focuses on environmentally safe and friendly products. We are looking for a tri-fold product brochure design that advertises a few different product types and services we offer.

Attachments:
1. I've included a document with all the text that needs to be included in the brochure. (Attachment: 150624 RV Brochure Text.docx)
2. I've also included a sample brochure that is currently used by one of our product Distributors, to give an idea of what the content should look like. (Attachment: BROCHURE SAMPLE.pdf)
3. I've included our company logo.

We are open to all design ideas.
Since we are an environmentally friendly company, we prefer to use earthy tones -- but are open to new suggestions.
Any graphics/photos included in the brochure should be construction related: asphalt trucks, paving

Target Market(s)

Construction companies, truckers

Industry/Entity Type

It Company

Font styles to use
Serif
Sans Serif

Requirements
Must have
• Please include all of the text in the attachment labeled: 1506 RV Brochure Text.docx
Nice to have
• We would like to use earthy tones - greens, blues, etc. since we are "environmentally friendly"

```html
<!DOCTYPE html>
<html lang="en">
<head>
<meta charset="utf-8">
<title>RV Solvents – Product Brochure Inside Spread</title>
<link rel="stylesheet" href="https://fonts.googleapis.com/css2?family=Open+Sans:wght@600;700&family=Crimson+Text:wght@400;700&display=swap">
<style>
  :root {
    --sky-top: #7f8b9a;
    --sky-mid: #c6ccd3;
    --haze: #d9d7cd;
    --field-warm: #b99a62;
    --field-green: #868246;
    --road: #4a4b4d;
    --mission-green: #5b6f4b;
    --heading-teal: #2a6370;
    --body-ink: #3a3a3a;
    --swoosh: #2d6b73;
    --ring: #6f675b;
    --badge-fill: #bfc27e;
    --badge-text: #f3efc8;
  }
  html, body {
    margin: 0;
    padding: 0;
    width: 1200px;
    height: 927px;
    overflow: hidden;
    background: #ffffff;
  }
  .spread {
    position: relative;
    width: 1200px;
    height: 927px;
    overflow: hidden;
  }
  .landscape-backdrop {
    position: absolute;
    inset: 0;
    background: linear-gradient(180deg,
      var(--sky-top) 0%,
      var(--sky-mid) 33%,
      var(--haze) 54%,
      var(--field-warm) 62%,
      var(--field-green) 71%,
      #6b6a4a 78%,
      #5c5c5a 81%,
      var(--road) 90%,
      #36373a 100%);
  }
  .swoosh-layer {
    position: absolute;
    inset: 0;
  }
  .mission {
    position: absolute;
    left: 68px;
    top: 58px;
    width: 300px;
    margin: 0;
    font-family: "Open Sans", sans-serif;
    font-weight: 600;
    font-size: 22.5px;
    line-height: 34px;
    color: var(--mission-green);
  }
  .column {
    position: absolute;
    top: 62px;
    width: 342px;
  }
  .column--release { left: 433px; }
  .column--cleaners { left: 836px; }
  .column h2 {
    margin: 0 0 14px;
    font-family: "Open Sans", sans-serif;
    font-weight: 700;
    font-size: 19px;
    line-height: 26px;
    color: var(--heading-teal);
  }
  .column p {
    margin: 0 0 16px;
    font-family: "Crimson Text", serif;
    font-size: 13.6px;
    line-height: 16px;
    color: var(--body-ink);
  }
  .column strong { font-weight: 700; }
  .badge-list {
    position: absolute;
    margin: 0;
    padding: 0 0 0 22px;
    font-family: "Open Sans", sans-serif;
    font-weight: 700;
    font-size: 15px;
    line-height: 19px;
    color: var(--badge-text);
  }
  .badge-list li { margin-bottom: 7px; }
  .badge-list--release { left: 516px; top: 554px; width: 190px; }
  .badge-list--cleaners { left: 922px; top: 472px; width: 190px; }
</style>
</head>
<body>
<main class="spread">
  <div class="landscape-backdrop" role="img" aria-label="Blurred photo of an open road running past autumn fields under a cloudy sky"></div>

  <svg class="swoosh-layer" width="1200" height="927" viewBox="0 0 1200 927" aria-hidden="true">
    <path d="M -12 285 C 45 500 210 680 470 667 C 610 660 650 522 790 522 C 910 522 985 575 1060 636 C 1135 697 1190 820 1212 910"
          fill="none" stroke="var(--swoosh)" stroke-width="15"/>
    <circle cx="600" cy="623" r="153" fill="var(--ring)"/>
    <circle cx="600" cy="623" r="132" fill="var(--badge-fill)"/>
    <circle cx="1029" cy="556" r="145" fill="var(--ring)"/>
    <circle cx="1029" cy="556" r="124" fill="var(--badge-fill)"/>
  </svg>

  <p class="mission">Our mission is to provide safe, effective, natural products at economical prices.&nbsp; Our products are made from renewable ingredients and are generally safe for you, your coworkers, and the environment.</p>

  <section class="column column--release">
    <h2>RV Asphalt Release Agents</h2>
    <p>RV Solvents asphalt release agents are the most <strong>effective</strong> release agents on the market. RV’s release agents works extremely well on polymer and “popcorn” asphalts. They are <strong>safe to touch, dilutable</strong>, and don’t require metering. Our products are <strong>environmentally safe</strong>, made from all renewable resources and replace the use of diesel fuel in truck beds to prevent loads from sticking.</p>
    <p>Our release agents work by adhering to the truck bed surface, <strong>creating a barrier</strong> between the surface applied to and the asphalt, so the asphalt does not stick. Unlike other products that must be diluted to preserve the integrity of the asphalt, RV’s products are <strong>safe enough to use at full strength,</strong> yet strong enough to dilute.</p>
    <p>RV Solvents also offers <strong>custom truck and plant spray systems</strong>. Systems can be fully automatic or push button/timer style reducing run-off and product waste.</p>
  </section>

  <section class="column column--cleaners">
    <h2>RV Tar Removers and Cleaners</h2>
    <p>RV offers several <strong>green solvents</strong> designed to clean and remove tar and asphalt off of pavers, trucks and tools. For tough jobs, our products can be used <strong>straight</strong> out of the container. Simply pour onto a rag or spray on surface and wipe clean. For lighter jobs, our products can be <strong>diluted</strong> with water or used in combination with a power washer.</p>
    <p><strong>Applications</strong> include removing tar off of truck frames and rims, de greasing engines, transmissions and final drives, removing bugs, tree sap and bird droppings from your vehicle’s finish, household cleaning and de greasing jobs and much more.</p>
  </section>

  <ul class="badge-list badge-list--release">
    <li>Works on modified and “popcorn” asphalts</li>
    <li>Non-toxic</li>
    <li>Water soluble</li>
    <li>Doesn’t stain clothes</li>
  </ul>

  <ul class="badge-list badge-list--cleaners">
    <li>For tough jobs, can be applied straight of the container.</li>
    <li>For lighter jobs, simply dilute or use with a power washer</li>
  </ul>
</main>
</body>
</html>
```